Professional services

we are preparing a flyer for an event to promote our new service. to use organge colour as background ( our corporate colour)

Header : Social Media Monitoring, Analytics and Engagement
text :
Leveraging on best of bred technologies, domain knowledge and oversea delivery centres, Vantrelle provides social media monitoring, analytic and engagement services.

This can be used for branding, online reputation, social CRM (sales, marketing & customer services), planning & measurement of campaign and research.

Please contact us at contactus@vantrelle-example.biz to explore more.

Industry/Entity Type

Marketing

```html
<!DOCTYPE html>
<html lang="en">
<head>
<meta charset="utf-8">
<title>Vantrelle – Social Media Monitoring, Analytics &amp; Engagement</title>
<link rel="stylesheet" href="https://fonts.googleapis.com/css2?family=Arimo:wght@400&display=swap">
<style>
  :root {
    --brand-orange: #f2561a;
    --brand-orange-deep: #e43a12;
    --brand-orange-light: #f98a2a;
    --title-red: #e8321e;
    --title-grey: #3a3a3a;
    --footer-grey: #4a4a4a;
    --paper: #ffffff;
    --text-light: #ffffff;
    --photo-top: #c9b3a6;
    --photo-mid: #8a8288;
    --photo-bottom: #4a4a50;
  }
  html, body {
    margin: 0;
    padding: 0;
    overflow: hidden;
    background: var(--paper);
  }
  .flyer {
    position: relative;
    width: 916px;
    height: 1200px;
    overflow: hidden;
    background: var(--paper);
    font-family: "Arimo", Arial, sans-serif;
  }
  .flyer__wave {
    position: absolute;
    inset: 0;
    width: 916px;
    height: 1200px;
  }
  .headline {
    position: absolute;
    top: 50px;
    left: 0;
    margin: 0;
    font-weight: 400;
    font-size: 58px;
    line-height: 71px;
  }
  .headline__line { display: block; white-space: nowrap; }
  .headline__line--lead { color: var(--title-red); padding-left: 30px; }
  .headline__line--second { color: var(--title-grey); padding-left: 111px; }
  .headline__line--third { color: var(--title-grey); padding-left: 178px; }

  .network-collage {
    position: absolute;
    left: 570px;
    top: 118px;
    width: 330px;
    height: 290px;
    border-radius: 10px;
    background: linear-gradient(160deg, #e9edf4 0%, #c9d5e6 45%, #dfe3ea 100%);
    transform: rotate(-4deg);
  }

  .portrait {
    position: absolute;
    left: 565px;
    top: 440px;
    width: 351px;
    height: 760px;
    border-radius: 14px 0 0 0;
    background: linear-gradient(180deg, var(--photo-top) 0%, var(--photo-mid) 40%, var(--photo-bottom) 100%);
  }

  .service-copy {
    position: absolute;
    left: 29px;
    top: 457px;
    width: 530px;
    margin: 0;
    color: var(--text-light);
    font-size: 41px;
    line-height: 51px;
  }
  .service-copy p { margin: 0 0 48px; }

  .contact {
    position: absolute;
    left: 29px;
    top: 1088px;
    color: var(--footer-grey);
  }
  .contact__label { margin: 0; font-size: 34px; line-height: 40px; }
  .contact__email { margin: 4px 0 0; font-size: 24px; line-height: 30px; }
</style>
</head>
<body>
<main class="flyer">
  <svg class="flyer__wave" viewBox="0 0 916 1200" aria-hidden="true">
    <defs>
      <linearGradient id="orangeField" x1="0" y1="0" x2="0" y2="1">
        <stop offset="0" stop-color="var(--brand-orange-light)"/>
        <stop offset="0.35" stop-color="var(--brand-orange)"/>
        <stop offset="1" stop-color="var(--brand-orange-deep)"/>
      </linearGradient>
    </defs>
    <path d="M0 330 C 180 330, 330 390, 520 380 C 700 370, 820 320, 916 300 L 916 1058 L 0 1058 Z" fill="url(#orangeField)"/>
    <path d="M0 360 C 160 330, 300 400, 500 395 C 680 390, 800 345, 916 330 L 916 360 C 800 372, 690 420, 500 425 C 300 430, 170 380, 0 400 Z" fill="#ffffff" opacity="0.35"/>
    <rect x="0" y="1058" width="916" height="142" fill="#ffffff"/>
  </svg>

  <h1 class="headline">
    <span class="headline__line headline__line--lead">Social Media Monitoring,</span>
    <span class="headline__line headline__line--second">Analytics &amp;</span>
    <span class="headline__line headline__line--third">Engagement</span>
  </h1>

  <div class="network-collage" role="img" aria-label="Stacked collage of social network badges"></div>

  <div class="portrait" role="img" aria-label="Photo of a smiling businesswoman in a grey suit working on a laptop"></div>

  <div class="service-copy">
    <p>Leveraging on best of bred technologies,</p>
    <p>Domain knowledge and oversea delivery centres,</p>
    <p>Vantrelle provides social media monitoring,</p>
    <p>Analytic &amp; engagement services.</p>
  </div>

  <footer class="contact">
    <p class="contact__label">Contact Us</p>
    <p class="contact__email">contactus@vantrelle-example.biz</p>
  </footer>
</main>
</body>
</html>
```